Video Company website for high tech video software company

Design a website for a software company that has an extensive list of products that process incoming TV video and video ads and processes the video for delivery to mobile phones, tablets, Set Top Boxes, and PCs.

Coding

Coded - Design and coding required

Number of Pages Required

1 page

```html
<!DOCTYPE html>
<html lang="en">
<head>
<meta charset="utf-8">
<title>NovaCast — OTT IPTV DVB Complete Solution</title>
<link href="https://fonts.googleapis.com/css2?family=Montserrat:wght@700&family=Roboto:wght@400;500;700&display=swap" rel="stylesheet">
<style>
  :root {
    --ink: #ffffff;
    --night: #02040a;
    --navy: #06163a;
    --deep: #0a2150;
    --accent: #1d8fef;
    --hero-glow: #1b4fa8;
    --card-top: #0b86cc;
    --card-bottom: #0a4b98;
  }
  * { margin: 0; padding: 0; box-sizing: border-box; }
  html, body { width: 805px; height: 1200px; overflow: hidden; background: var(--night); }
  .page {
    position: relative; width: 805px; height: 1200px; overflow: hidden;
    font-family: "Roboto", Arial, sans-serif; color: var(--ink);
    background:
      radial-gradient(ellipse 600px 220px at 300px 1010px, rgba(25,70,150,.6), transparent 70%),
      linear-gradient(180deg, #000 0%, #020611 12%, var(--navy) 30%, #040c22 42%, var(--deep) 62%, #081a44 82%, var(--night) 100%);
  }
  .brand {
    position: absolute; font-family: "Roboto", Arial, sans-serif; font-weight: 700;
    color: var(--ink); display: flex; align-items: center; gap: 6px;
  }
  .brand .mark { width: 12px; height: 12px; background: var(--accent); }
  .brand--header { left: 57px; top: 26px; font-size: 24px; }
  .brand--footer { left: 0; right: 0; top: 1100px; justify-content: center; font-size: 30px; }
  .brand--footer .mark { width: 15px; height: 15px; }
  .nav { position: absolute; top: 29px; left: 478px; display: flex; gap: 29px; list-style: none; }
  .nav a { color: var(--ink); text-decoration: none; font-size: 11px; font-weight: 500; }
  .hero-title {
    position: absolute; top: 93px; left: 0; right: 0; text-align: center;
    font-family: "Montserrat", Arial, sans-serif; font-weight: 700; font-size: 20.5px;
    color: var(--accent);
  }
  .hero-art {
    position: absolute; left: 0; top: 130px; width: 805px; height: 270px;
    background:
      radial-gradient(ellipse 420px 40px at 400px 100px, rgba(80,170,255,.45), transparent 75%),
      radial-gradient(ellipse 520px 150px at 400px 170px, rgba(30,80,170,.6), transparent 75%),
      linear-gradient(180deg, transparent 0%, rgba(20,60,140,.35) 50%, transparent 100%);
  }
  .pipeline-label {
    position: absolute; font-size: 12.5px; font-weight: 500; line-height: 14px;
    text-align: center; transform: translateX(-50%); white-space: nowrap;
  }
  .headline {
    position: absolute; top: 423px; left: 0; right: 0; text-align: center;
    font-size: 20.5px; font-weight: 700; line-height: 30px; color: var(--accent);
  }
  .features {
    position: absolute; left: 67px; top: 516px; width: 671px;
    display: grid; grid-template-columns: repeat(3, 213px); grid-auto-rows: 163px;
    column-gap: 16px; row-gap: 17px;
  }
  .feature {
    background: linear-gradient(160deg, var(--card-top) 0%, #0967b4 50%, var(--card-bottom) 100%);
    text-align: center; padding-top: 30px;
  }
  .feature h2 { font-size: 22px; font-weight: 700; line-height: 26px; margin-bottom: 3px; }
  .feature p { font-size: 15.8px; line-height: 22.6px; }
  .feature--sms { padding-top: 33px; }
  .copyright {
    position: absolute; top: 1164px; left: 0; right: 0; text-align: center; font-size: 11px;
  }
</style>
</head>
<body>
<div class="page">
  <header>
    <div class="brand brand--header"><span>NovaCast</span><span class="mark"></span></div>
    <ul class="nav">
      <li><a href="#">PRODUCTS</a></li>
      <li><a href="#">RESOURCES</a></li>
      <li><a href="#">TEAM</a></li>
      <li><a href="#">CONTACT</a></li>
    </ul>
  </header>

  <h1 class="hero-title">OTT IPTV DVB COMPLETE SOLUTION</h1>

  <div class="hero-art" role="img" aria-label="Illustration of a satellite head-end sending a glowing video stream through processing stages to phones, tablets, set top boxes and TVs over a dotted digital landscape"></div>

  <div class="pipeline-label" style="left:152px;top:168px">TRANSCODING</div>
  <div class="pipeline-label" style="left:310px;top:168px">SUBSCRIBER<br>MANGEMENT</div>
  <div class="pipeline-label" style="left:459px;top:181px">STREAMING</div>
  <div class="pipeline-label" style="left:620px;top:181px">APPS</div>
  <div class="pipeline-label" style="left:224px;top:276px">MIDDLEWARE</div>
  <div class="pipeline-label" style="left:386px;top:276px;text-align:left">CAS/DRM<br>SECURITY</div>
  <div class="pipeline-label" style="left:553px;top:276px">TARGETED ADS</div>

  <h2 class="headline">A HIGH-QUALITY HIGH-DENSITY 150 CHANNEL<br>IPTV/OTT SYSTEM IN 2RU WITH 24/7 RELIABLITY</h2>

  <section class="features">
    <article class="feature"><h2>COMPLETE</h2><p>Apps with Live TV<br>Catchup TV + VOD<br>Middleware + Ads</p></article>
    <article class="feature"><h2>MSO SCALE</h2><p>Nationwide Distribution<br>Cloud or on premise<br>Distributed head-ends</p></article>
    <article class="feature"><h2>RELIABLE</h2><p>24/7 Operation<br>24/7 System Monitoring<br>MPEG Video Inspection</p></article>
    <article class="feature"><h2>CAS / DRM</h2><p>Hollywood approved<br>Highly secure for<br>IPTV/OTT/DVB systems</p></article>
    <article class="feature"><h2>STREAMING</h2><p>High Capacity<br>Edge Caching<br>No 3rd party CDN needed</p></article>
    <article class="feature"><h2>TRANSCODING</h2><p>High Quality<br>High Density<br>4K/8K Full HD &amp; SD</p></article>
    <article class="feature"><h2>ADVERTISING</h2><p>Targeted Ads<br>Ad analytics<br>Advertiser Portal</p></article>
    <article class="feature"><h2>MIDDLEWARE</h2><p>Live TV with EPG<br>VOD + CDN<br>Catchup TV</p></article>
    <article class="feature feature--sms"><h2>SMS</h2><p>MSO Grade Subscriber<br>Management<br>for IPTV/OTT/DVB</p></article>
  </section>

  <footer>
    <div class="brand brand--footer"><span>NovaCast</span><span class="mark"></span></div>
    <p class="copyright">© 2021 NovaCast, Inc. All Rights Reserved.</p>
  </footer>
</div>
</body>
</html>
```